RWT Business Cards

We need to design new business cards for our company. We are a Managed Discretionary Account (MDA) adviser based in Sydney Australia. We have distinct corporate colour pallet which will be provided and various logo formats. I will also include our current business card design as a guide only to what we have accepted previously. The final design should convey financial professionalism and experience as well as the necessary company information.

Target Market(s)

High Net Worth and Professional Investors

Industry/Entity Type

Financial

Font styles to use
Serif

```html
<!DOCTYPE html>
<html lang="en">
<head>
<meta charset="utf-8">
<title>RWT Business Cards</title>
<link rel="stylesheet" href="https://fonts.googleapis.com/css2?family=Libre+Caslon+Text:wght@400;700&family=Open+Sans:wght@400;600&display=swap">
<style>
  :root {
    --bg: #ecebe7;
    --green-dark: #0b7a45;
    --green: #12955a;
    --green-light: #1aa96a;
    --white: #ffffff;
    --paper: #f7f7f6;
    --grey: #6f7470;
  }
  * { box-sizing: border-box; margin: 0; padding: 0; }
  html, body {
    width: 1200px; height: 1023px; overflow: hidden;
    background: var(--bg);
  }
  .sheet {
    width: 1200px; height: 1023px;
    display: flex; flex-direction: column; align-items: center; justify-content: center;
    gap: 70px;
  }
  .card {
    width: 620px; height: 354px;
    border-radius: 6px;
    box-shadow: 0 10px 30px rgba(0,0,0,0.18);
    position: relative; overflow: hidden;
  }
  /* Front */
  .card-front {
    background: linear-gradient(135deg, var(--green-dark) 0%, var(--green) 50%, var(--green-light) 100%);
    color: var(--white);
    display: flex; flex-direction: column; align-items: center; justify-content: center;
  }
  .company-name {
    font-family: "Libre Caslon Text", serif;
    font-size: 36px; font-weight: 400; letter-spacing: 1px;
    line-height: 1.25; text-align: center; color: var(--white);
    text-transform: uppercase;
  }
  .website {
    margin-top: 34px; font-family: "Open Sans", sans-serif;
    font-size: 13px; letter-spacing: 4px;
  }
  /* Back */
  .card-back {
    background: var(--paper);
    font-family: "Libre Caslon Text", serif;
  }
  .accent-bar {
    position: absolute; left: 0; top: 40px; width: 10px; height: 64px;
    background: var(--green); border-radius: 0 5px 5px 0;
  }
  .holder { position: absolute; left: 40px; top: 40px; }
  .holder-name { color: var(--green); font-size: 30px; font-weight: 700; }
  .holder-title {
    color: var(--grey); font-family: "Open Sans", sans-serif; font-size: 13px; margin-top: 4px;
  }
  .registrations {
    position: absolute; left: 40px; bottom: 36px;
    font-family: "Open Sans", sans-serif; font-size: 12px; color: var(--grey); line-height: 1.7;
  }
  .registrations b { color: var(--green); font-weight: 600; }
  .bottom-band {
    position: absolute; left: 0; right: 0; bottom: 0; height: 8px; background: var(--green);
  }
</style>
</head>
<body>
  <main class="sheet">
    <section class="card card-front" aria-label="Card front">
      <div class="company-name">Riverwell Capital<br>Partners</div>
      <div class="website">www.riverwellcapital.com.au</div>
    </section>

    <section class="card card-back" aria-label="Card back">
      <div class="accent-bar"></div>
      <div class="holder">
        <div class="holder-name">Daniel Hart</div>
        <div class="holder-title">Managing Director</div>
        <div class="holder-title">Chief Investment Officer</div>
      </div>
      <div class="registrations">
        <div><b>ABN:</b> 41 207 583 916</div>
        <div><b>AFSL:</b> 518204</div>
      </div>
      <div class="bottom-band"></div>
    </section>
  </main>
</body>
</html>
```